Pitch deck for fundraising for a timber drying business

We have the basic content in a powerpoint but need someone to take that and make an attractive and engaging document for a reader who may see hundreds of these a week so visual impact is key.
We are launching a timber drying business in Australia using an exclusive line of kilns not otherwise available in Australia.
Designs should focus on natural tones and connections with forests and timber, probably with a green (colour) focus.
Updates

Sick

Target Market(s)

investors, wealthyindividuals

Colors

Designer to choose colors to be used in the design.

Requirements
Nice to have
• Design in Canva or similar

```html
<!DOCTYPE html>
<html lang="en">
<head>
<meta charset="utf-8">
<title>Hardwood Ventures – Pitch Deck, Second Part</title>
<link href="https://fonts.googleapis.com/css2?family=Titillium+Web:wght@400;600;700&family=Carlito:wght@400;700&family=Arimo:wght@400&display=swap" rel="stylesheet">
<style>
:root{
  --canvas:#f1f1f1;
  --paper:#ffffff;
  --green:#5a822f;
  --green-bar:#5b8236;
  --green-mid:#8aa84f;
  --green-light:#b5cf8f;
  --ink:#222222;
  --muted:#555555;
  --rule:#b8b8b8;
  --panel:#f2f2f2;
  --row-alt:#f0f0f0;
}
*{box-sizing:border-box;margin:0;padding:0}
html,body{width:1200px;height:1200px;overflow:hidden;background:var(--canvas)}
body{position:relative;font-family:"Carlito",sans-serif;color:var(--ink)}

.slide{position:absolute;width:850px;height:638px;background:var(--paper);transform:scale(0.6212);transform-origin:top left;overflow:hidden}
.slide--treads{left:55px;top:60px}
.slide--plan{left:621px;top:61px}
.slide--financials{left:55px;top:495px;width:852px;height:639px}
.slide--risk{left:621px;top:495px;width:848px;height:636px}

.slide__title{position:absolute;left:22px;top:30px;font-family:"Titillium Web",sans-serif;font-weight:700;font-size:40px;letter-spacing:.5px;color:var(--green);line-height:1.2}
.slide__rule{position:absolute;left:22px;right:20px;top:87px;height:1px;background:var(--rule)}
.slide__page{position:absolute;right:30px;bottom:20px;font-size:13px;color:var(--muted)}

/* Why stair treads */
.reason{position:absolute;display:flex;align-items:center;font-family:"Titillium Web",sans-serif;font-size:18px;line-height:23px}
.reason__num{width:61px;flex:none;font-size:38px;font-weight:600;color:var(--green);padding-left:5px}
.reason__text{width:320px}
.reason__text b{font-weight:600}
.treads__divider{position:absolute;left:425px;top:115px;width:1px;height:287px;background:var(--rule)}
.treads__photo{position:absolute;left:0;top:431px;width:100%;height:207px;background:linear-gradient(180deg,#cfe3a8 0%,#7c9e45 35%,#34481c 70%,#5d7a2c 100%)}

/* Business plan */
.plan-card{position:absolute;top:103px;width:249px}
.plan-card__frame{height:192px;border:1px solid #d6d6d6;border-bottom:5px solid var(--green-bar);padding:9px 9px 10px}
.plan-card__photo{width:100%;height:168px}
.plan-card__photo--hall{background:linear-gradient(180deg,#4a4a48 0%,#7b7a74 45%,#a59f92 100%)}
.plan-card__photo--kiln{background:linear-gradient(180deg,#8fa3b2 0%,#23303d 40%,#111a22 100%)}
.plan-card__photo--line{background:linear-gradient(180deg,#3b3d40 0%,#9aa0a2 50%,#d8d3bd 100%)}
.plan-card__heading{margin-top:16px;font-family:"Titillium Web",sans-serif;font-weight:600;font-size:20px;color:var(--green);line-height:22px}
.plan-card__body{margin-top:6px;font-size:14.5px;line-height:17px;color:var(--ink)}
.plan-card__body p+p{margin-top:5px}
.plan__note{position:absolute;left:22px;top:586px;font-size:10.5px;color:var(--muted)}

/* Financials */
.fin-panel{position:absolute;left:0;top:123px;width:405px;height:444px;background:var(--panel)}
.fin-timeline{position:absolute;left:35px;top:160px;width:0;height:304px;border-left:1px dotted #9a9a9a}
.fin-point{position:absolute;left:63px;width:320px;font-size:17.5px;line-height:20px}
.fin-point::before{content:"";position:absolute;left:-40px;top:1px;width:18px;height:18px;border-radius:50%;background:var(--green-mid);box-shadow:0 0 0 3px #d3e1bd}
.fin-chart{position:absolute;left:426px;top:125px;width:404px;height:241px;border:1px solid #a7a7a7;background:#fff}
.fin-table{position:absolute;left:426px;top:379px;width:404px;border-collapse:collapse;font-size:14.5px}
.fin-table th{background:var(--green-bar);color:#fff;font-family:"Titillium Web",sans-serif;font-weight:600;font-size:19px;height:39px;text-align:left}
.fin-table td{height:35px;padding-left:9px;line-height:16px}
.fin-table tr:nth-child(even) td{background:var(--row-alt)}
.fin-table tr:last-child td{height:44px;border-bottom:3px solid var(--green-bar)}

/* Risk */
.risk-table{position:absolute;left:21px;top:107px;width:805px;border-collapse:collapse}
.risk-table th{background:var(--green-bar);color:#fff;font-family:"Titillium Web",sans-serif;font-weight:600;font-size:22px;height:45px;text-align:left;padding-left:9px}
.risk-table th:first-child{border-right:2px solid #fff}
.risk-table td{padding:0 10px 0 9px;vertical-align:middle}
.risk-table td:first-child{width:236px;font-weight:700;font-size:18px;line-height:21px;border-right:2px solid #fff}
.risk-table td:last-child{font-size:14.5px;line-height:17px}
.risk-table tbody tr:nth-child(even) td{background:var(--row-alt)}
.risk-table tbody tr:last-child td{border-bottom:3px solid var(--green-bar)}

.part-label{position:absolute;left:26px;top:1082px;font-family:"Arimo",sans-serif;font-size:76px;color:#000;line-height:1}
</style>
</head>
<body>

<!-- Why stair treads -->
<section class="slide slide--treads">
  <h2 class="slide__title">WHY STAIR TREADS</h2>
  <div class="slide__rule"></div>
  <div class="treads__divider"></div>

  <div class="reason" style="left:0;top:118px"><span class="reason__num">01</span><span class="reason__text">XX% margin</span></div>
  <div class="reason" style="left:0;top:195px"><span class="reason__num">02</span><span class="reason__text">Standardised product allowing <b>optimisation</b> of production processes</span></div>
  <div class="reason" style="left:0;top:303px"><span class="reason__num">03</span><span class="reason__text"><b>Installers looking for alternatives</b> – ~30% of Corvell products out of specification resulting in no installer profit on those jobs</span></div>

  <div class="reason" style="left:430px;top:116px"><span class="reason__num">04</span><span class="reason__text"><b>High absolute $ returns</b> – ~$XXXm3 profit</span></div>
  <div class="reason" style="left:430px;top:195px"><span class="reason__num">05</span><span class="reason__text"><b>Large market</b> – over 65 potential clients indicated interest in purchasing in Sydney alone <sup style="font-size:9px">1</sup></span></div>
  <div class="reason" style="left:430px;top:303px"><span class="reason__num">06</span><span class="reason__text"><b>Significant drying time advantage</b> over competitors: 1 week v 7-8 months</span></div>

  <div class="treads__photo" role="img" aria-label="Photo of a sunlit forest of tall tree trunks with green undergrowth"></div>
</section>

<!-- Business plan -->
<section class="slide slide--plan">
  <h2 class="slide__title">BUSINESS PLAN</h2>
  <div class="slide__rule"></div>

  <article class="plan-card" style="left:21px">
    <div class="plan-card__frame"><div class="plan-card__photo plan-card__photo--hall" role="img" aria-label="Photo of an empty warehouse interior with steel roof"></div></div>
    <h3 class="plan-card__heading">ESTABLISHMENT</h3>
    <div class="plan-card__body">
      <p>Rent 300m2+ warehouse space in Coffs Harbour – central to north coast hardwood forests. A site will be selected once an ETA for the initial kiln is established. Initial lease term 6 months with options for further terms of 3 years.</p>
      <p>An example: 747m2 factory and hardstand in Coffs Harbour $36,000pa<sup style="font-size:8px">1</sup></p>
      <p>We are also in preliminary discussions to lease a small sawmill as an alternative.</p>
    </div>
  </article>

  <article class="plan-card" style="left:301px">
    <div class="plan-card__frame"><div class="plan-card__photo plan-card__photo--kiln" role="img" aria-label="Photo of a dark container-style drying kiln"></div></div>
    <h3 class="plan-card__heading">DRYVEX TRIAL</h3>
    <div class="plan-card__body">
      <p>In order to minimise risk and reduce lead time (6 v 14 weeks) on the first machine we will order an Dryvex Plus ($US79K) to undertake initial production.</p>
      <p>We will have conducted 2 production runs within the first month and will then decide whether to order an Dryvex Turbo (up to 14-week lead time) or undertake further testing.</p>
    </div>
  </article>

  <article class="plan-card" style="left:581px">
    <div class="plan-card__frame"><div class="plan-card__photo plan-card__photo--line" role="img" aria-label="Photo of a bright factory floor with timber stacked on racks"></div></div>
    <h3 class="plan-card__heading">SCALING PRODUCTION</h3>
    <div class="plan-card__body" style="letter-spacing:-.2px">
      <p>Following the successful trial of the Dryvex Plus we will purchase an Dryvex Turbo as it has 380% greater throughput (being 50% larger and twice as fast to dry). Whilst more expensive, Turbos minimise the amount of labour in loading and reduce the floor space required for a given level of output.</p>
      <p>We propose to acquire all future equipment debt free and it is likely that our growth will only be constrained by the availability of Dryvex Turbos and the seasonal availability of timber.</p>
    </div>
  </article>

  <p class="plan__note"><sup>1</sup> https://www.leasefinder.com.au/for-lease/property-12-mill-road-coffs-harbour-nsw-2450-100284517</p>
  <span class="slide__page">6</span>
</section>

<!-- Financials -->
<section class="slide slide--financials">
  <h2 class="slide__title">FINANCIALS</h2>
  <div class="slide__rule"></div>

  <div class="fin-panel"></div>
  <div class="fin-timeline"></div>
  <p class="fin-point" style="top:150px">Hardwood Ventures will offer investors high levels of cash returns with the business netting around $XXK pm with just the Dryvex Plus and almost $XXK pm with a Plus and a Turbo in month 7.</p>
  <p class="fin-point" style="top:277px">From there we will ramp up production capacity in accordance with sales and Dryvex production capacity.</p>
  <p class="fin-point" style="top:363px">We view HVI as a long term hold, paying out 80%+ of net profit where there aren’t opportunities to grow the business.</p>
  <p class="fin-point" style="top:452px">By the time we have 10 total kilns (end of year 3) we expect to be distributing a total of approximately $XX per month and retaining $XXK pm.</p>

  <svg class="fin-chart" viewBox="0 0 404 241" role="img" aria-label="Bar chart of revenue and EBITDA for years 1 to 3">
    <g font-family="Carlito, sans-serif" font-size="10" fill="#333" text-anchor="end">
      <text x="66" y="15">$30,000,000</text>
      <text x="66" y="49">$25,000,000</text>
      <text x="66" y="82">$20,000,000</text>
      <text x="66" y="116">$15,000,000</text>
      <text x="66" y="149">$10,000,000</text>
      <text x="66" y="183">$5,000,000</text>
      <text x="60" y="216">$-</text>
    </g>
    <g stroke="#d9d9d9" stroke-width="1">
      <line x1="78" y1="12" x2="325" y2="12"/>
      <line x1="78" y1="45.5" x2="325" y2="45.5"/>
      <line x1="78" y1="79" x2="325" y2="79"/>
      <line x1="78" y1="112.5" x2="325" y2="112.5"/>
      <line x1="78" y1="146" x2="325" y2="146"/>
      <line x1="78" y1="179.5" x2="325" y2="179.5"/>
    </g>
    <line x1="78" y1="213" x2="325" y2="213" stroke="#8c8c8c"/>
    <line x1="78" y1="10" x2="78" y2="213" stroke="#8c8c8c"/>
    <g fill="var(--green-mid)">
      <rect x="96" y="189" width="24" height="24"/>
      <rect x="179" y="107" width="24" height="106"/>
      <rect x="262" y="38" width="24" height="175"/>
    </g>
    <g fill="var(--green-light)">
      <rect x="120" y="202" width="24" height="11"/>
      <rect x="203" y="153" width="24" height="60"/>
      <rect x="286" y="113" width="24" height="100"/>
    </g>
    <g font-family="Carlito, sans-serif" font-size="10" fill="#333" text-anchor="middle">
      <text x="120" y="230">Year 1</text>
      <text x="203" y="230">Year 2</text>
      <text x="286" y="230">Year 3</text>
    </g>
    <rect x="343" y="106" width="6" height="6" fill="var(--green-mid)"/>
    <rect x="343" y="126" width="6" height="6" fill="var(--green-light)"/>
    <g font-family="Carlito, sans-serif" font-size="10" fill="#333">
      <text x="352" y="113">Revenue</text>
      <text x="352" y="133">EBITDA</text>
    </g>
  </svg>

  <table class="fin-table">
    <thead><tr><th style="width:140px"></th><th style="width:98px">Year 1</th><th style="width:94px">Year 2</th><th>Year 3</th></tr></thead>
    <tbody>
      <tr><td colspan="4">EBITDA</td></tr>
      <tr><td colspan="4">Cumulative cash</td></tr>
      <tr><td colspan="4">No. kilns</td></tr>
      <tr><td colspan="4">Monthly<br>Recurring Profit</td></tr>
    </tbody>
  </table>
  <span class="slide__page">7</span>
</section>

<!-- Risk -->
<section class="slide slide--risk">
  <h2 class="slide__title">RISK</h2>
  <div class="slide__rule"></div>

  <table class="risk-table">
    <thead><tr><th>Risk</th><th>Mitigation</th></tr></thead>
    <tbody>
      <tr style="height:68px"><td>Disruption to log supply</td><td>Coffs Harbour is central to the hardwood timber forests of the north coast, allowing HVI to economically draw timber from a wider geographic area reducing the potential for localised issues such as weather or fires to impact supply.</td></tr>
      <tr style="height:58px"><td>Unable to obtain boards from sawmills</td><td>Diversify supply of boards, contract with state and private forests for own supply of logs and use contract sawmilling, Phase 3 develop own sawmilling capacity</td></tr>
      <tr style="height:70px"><td>Timber boards not to specification</td><td>Inspect and test delivered timber pre-drying to allow rejection of out of specification boards. Inspect post-drying boards to ensure they meet specification. Consider independent testing as part of out-bound QA process.</td></tr>
      <tr style="height:68px"><td>Kiln doesn’t perform to expectations</td><td>Warranty and product support for a fault. If operation of machine does not achieve expected levels of output increase number of machines or air-dry timber before placement in kiln to reduce kiln times.</td></tr>
      <tr style="height:70px"><td>Ability to supply required species timber</td><td>We will initially only dry loads of the most commonly used timber - blackbutt. As capacity and confidence in quality improve we will start to broaden the range of species we dry, this will also help mitigate any risks around supply of timber.</td></tr>
      <tr style="height:86px"><td>Copycat competitor</td><td>Our exclusive agreement for the supply of Dryvex equipment excludes direct competition in he short term but there are alternative kilns but with lesser performance.<br>Phase 2 of the strategic plan is focussed on developing a highly connected and integrated sales channel with the market in order to create a barrier to entry.</td></tr>
    </tbody>
  </table>
  <span class="slide__page">8</span>
</section>

<p class="part-label">Second Part</p>

</body>
</html>
```